Business card for my company-RMK Design Studio

I do not have a logo-I like red and keeping it clean. Information that should be on the card:
Tom Brakefield AIA
Architecture Planning Interiors
Cell Phone-614.492.5068
email-rmkarchitect1@lunvale.com
www.rmkdesignstudio.net

```html
<!DOCTYPE html>
<html lang="en">
<head>
<meta charset="utf-8">
<title>RMK Design Studio — Business Card</title>
<link rel="stylesheet" href="https://fonts.googleapis.com/css2?family=EB+Garamond:wght@400;600&display=swap">
<style>
  :root {
    --backdrop: #2b2b2d;
    --frame-red: #e31b23;
    --brand-red: #9e1016;
    --name-red: #d8141c;
    --paper-light: #ffffff;
    --paper-shade: #e6e6e6;
    --ink-grey: #4a4a4a;
    --shadow: rgba(0, 0, 0, 0.45);
  }
  * { box-sizing: border-box; margin: 0; padding: 0; }
  html, body {
    width: 1200px;
    height: 900px;
    overflow: hidden;
    background: var(--backdrop);
    font-family: "EB Garamond", Garamond, serif;
  }
  .canvas {
    position: relative;
    width: 1200px;
    height: 900px;
  }
  .card {
    position: absolute;
    left: 290px;
    width: 620px;
    height: 354px;
    background: var(--frame-red);
    padding: 16px;
    box-shadow: 0 18px 40px var(--shadow);
  }
  .card--front { top: 60px; }
  .card--back  { top: 486px; }
  .card__face {
    position: relative;
    width: 100%;
    height: 100%;
    background: linear-gradient(110deg, var(--paper-shade) 0%, #f2f2f2 45%, var(--paper-light) 100%);
  }
  .brand {
    display: flex;
    align-items: center;
    gap: 12px;
    color: var(--brand-red);
    font-weight: 600;
    white-space: nowrap;
  }
  .brand__square {
    display: block;
    background: var(--frame-red);
  }
  .card--front .brand {
    position: absolute;
    left: 50%;
    top: 50%;
    transform: translate(-50%, -50%);
    font-size: 38px;
  }
  .card--front .brand__square { width: 30px; height: 30px; }
  .card--back .brand {
    position: absolute;
    right: 36px;
    top: 40px;
    font-size: 26px;
  }
  .card--back .brand__square { width: 22px; height: 22px; }
  .holder {
    position: absolute;
    left: 52px;
    top: 150px;
  }
  .holder__name {
    color: var(--name-red);
    font-weight: 600;
    font-size: 25px;
    line-height: 1.1;
  }
  .holder__title {
    color: var(--ink-grey);
    font-size: 17px;
    margin-top: 2px;
    margin-left: 14px;
  }
  .contacts {
    position: absolute;
    left: 80px;
    top: 232px;
    list-style: none;
    color: var(--ink-grey);
    font-size: 17px;
  }
  .contacts__item {
    display: flex;
    align-items: center;
    gap: 10px;
    height: 26px;
  }
  .contacts__item:nth-child(2) { margin-left: 10px; }
  .contacts__item:nth-child(3) { margin-left: 20px; }
  .contacts__icon { width: 14px; height: 14px; flex: none; }
</style>
</head>
<body>
<main class="canvas">
  <section class="card card--front" aria-label="Card front">
    <div class="card__face">
      <div class="brand"><span class="brand__square"></span>RMK Design Studio</div>
    </div>
  </section>

  <section class="card card--back" aria-label="Card back">
    <div class="card__face">
      <div class="brand"><span class="brand__square"></span>RMK Design Studio</div>

      <div class="holder">
        <p class="holder__name">Tom Brakefield AIA</p>
        <p class="holder__title">Architecture Planning Interiors</p>
      </div>

      <ul class="contacts">
        <li class="contacts__item">
          <svg class="contacts__icon" viewBox="0 0 14 14" aria-hidden="true">
            <rect x="3.5" y="0.8" width="7" height="12.4" rx="1.2" fill="none" stroke="#9e1016" stroke-width="1.4"/>
            <line x1="6" y1="11" x2="8" y2="11" stroke="#9e1016" stroke-width="1.2"/>
          </svg>
          614.492.5068
        </li>
        <li class="contacts__item">
          <svg class="contacts__icon" viewBox="0 0 14 14" aria-hidden="true">
            <rect x="0.5" y="3" width="13" height="9" fill="#9e1016"/>
            <polyline points="0.8,3.4 7,8.2 13.2,3.4" fill="none" stroke="#fff" stroke-width="1.1"/>
          </svg>
          rmkarchitect1@lunvale.com
        </li>
        <li class="contacts__item">
          <svg class="contacts__icon" viewBox="0 0 14 14" aria-hidden="true">
            <circle cx="7" cy="7" r="6.2" fill="none" stroke="#9e1016" stroke-width="1.4"/>
            <ellipse cx="7" cy="7" rx="2.6" ry="6.2" fill="none" stroke="#9e1016" stroke-width="1"/>
            <line x1="0.8" y1="7" x2="13.2" y2="7" stroke="#9e1016" stroke-width="1"/>
          </svg>
          www.rmkdesignstudio.net
        </li>
      </ul>
    </div>
  </section>
</main>
</body>
</html>
```